Need a webinar banner promo to place on social media

We are organise a series of webinars in coming months.

We need a webinar banner design to be posted on Facebook and linkedin. The banner is for our webinar titled: Ways to Debut a Novel with Sparkle and Flair.

our website is www.quillmarket.com.au

there is a link on the website to the webinar registration for your reference.

```html
<!DOCTYPE html>
<html lang="en">
<head>
<meta charset="utf-8">
<title>Quill Market – Webinar Banners</title>
<link rel="stylesheet" href="https://fonts.googleapis.com/css2?family=Barlow+Condensed:ital,wght@1,500;1,600;1,700;1,800&family=Barlow:ital,wght@1,800&family=Montserrat:ital,wght@0,600;1,300&family=Poppins:wght@500&display=swap">
<style>
  :root{
    --page:#0a2a4f;
    --navy:#0a2345;
    --navy-deep:#061832;
    --white:#ffffff;
    --gold-dark:#b8862a;
    --gold-light:#f3e27a;
    --label:#5383c4;
  }
  html,body{margin:0;padding:0;width:1200px;height:1200px;overflow:hidden;background:var(--page);}
  .board{position:relative;width:1200px;height:1200px;}
  .banner{position:absolute;display:block;}
  .banner--facebook{left:197px;top:168px;width:805px;height:353px;}
  .banner--linkedin{left:76px;top:648px;width:1048px;height:342px;}
  .board-label{
    position:absolute;margin:0;
    font-family:"Montserrat",sans-serif;font-style:italic;font-weight:300;
    font-size:20px;letter-spacing:8px;color:var(--label);line-height:1;
  }
  .board-label--facebook{right:200px;top:538px;}
  .board-label--linkedin{left:81px;top:1010px;}
  .t-webinar{font-family:"Barlow",sans-serif;font-style:italic;font-weight:800;fill:var(--white);}
  .t-time{font-family:"Barlow Condensed",sans-serif;font-style:italic;font-weight:600;fill:var(--white);}
  .t-time-zone{fill:url(#goldText);}
  .t-kicker{font-family:"Barlow Condensed",sans-serif;font-style:italic;font-weight:500;}
  .t-headline{font-family:"Barlow Condensed",sans-serif;font-style:italic;font-weight:700;fill:var(--navy);}
  .t-day{font-family:"Barlow Condensed",sans-serif;font-style:italic;font-weight:800;fill:var(--navy);}
  .t-month{font-family:"Barlow Condensed",sans-serif;font-style:italic;font-weight:700;fill:var(--white);}
  .t-register{font-family:"Barlow Condensed",sans-serif;font-style:italic;font-weight:800;fill:var(--navy);}
  .t-url{font-family:"Poppins",sans-serif;font-weight:500;fill:var(--white);}
  .t-brand{font-family:"Barlow Condensed",sans-serif;font-style:italic;font-weight:700;fill:var(--gold-light);}
</style>
</head>
<body>
<div class="board">

  <svg width="0" height="0" style="position:absolute" aria-hidden="true">
    <defs>
      <linearGradient id="goldFill" x1="0" y1="0" x2="1" y2="0">
        <stop offset="0" stop-color="#b8862a"/>
        <stop offset="0.5" stop-color="#f3e27a"/>
        <stop offset="1" stop-color="#c08f2c"/>
      </linearGradient>
      <linearGradient id="goldText" x1="0" y1="0" x2="1" y2="0">
        <stop offset="0" stop-color="#b8862a"/>
        <stop offset="0.6" stop-color="#e8c85a"/>
        <stop offset="1" stop-color="#c9a03a"/>
      </linearGradient>
      <linearGradient id="goldBox" x1="0" y1="0" x2="0" y2="1">
        <stop offset="0" stop-color="#f3e27a"/>
        <stop offset="1" stop-color="#b8862a"/>
      </linearGradient>
      <linearGradient id="photoTone" x1="0" y1="0" x2="1" y2="1">
        <stop offset="0" stop-color="#050608"/>
        <stop offset="0.55" stop-color="#0b1426"/>
        <stop offset="1" stop-color="#1a2848"/>
      </linearGradient>
    </defs>
  </svg>

  <!-- Facebook banner -->
  <svg class="banner banner--facebook" viewBox="0 0 1296 569">
    <rect width="1296" height="569" fill="var(--white)"/>
    <polygon points="0,0 603,0 505,569 0,569" fill="var(--navy)"/>
    <polygon role="img" aria-label="Photo of a speaker at a lectern addressing a seated audience in a dark auditorium" points="0,0 503,0 399,569 0,569" fill="url(#photoTone)"/>
    <polygon points="499,0 507,0 403,569 395,569" fill="url(#goldBox)"/>
    <text class="t-brand" x="258" y="130" text-anchor="middle" font-size="78">QUILL</text>
    <text class="t-brand" x="258" y="205" text-anchor="middle" font-size="78">MARKET</text>

    <polygon points="518,62 865,62 855,134 508,134" fill="url(#goldFill)"/>
    <text class="t-webinar" x="686" y="113" text-anchor="middle" font-size="44" letter-spacing="14">WEBINAR</text>
    <polygon points="875,62 1296,62 1296,134 865,134" fill="var(--navy)"/>
    <text class="t-time" x="1073" y="113" text-anchor="middle" font-size="40">7:00 PM – 8:00 PM <tspan class="t-time-zone">AEDT</tspan></text>

    <text class="t-kicker" x="603" y="210" font-size="56" fill="url(#goldText)">WAYS TO DEBUT A NOVEL</text>
    <rect x="603" y="218" width="635" height="3" fill="var(--navy)"/>
    <text class="t-headline" x="588" y="308" font-size="96">WITH SPARKLE</text>
    <text class="t-headline" x="578" y="395" font-size="96">&amp; FLAIR</text>

    <polygon points="1118,220 1238,220 1213,406 1093,406" fill="var(--navy)"/>
    <polygon points="1129,227 1231,227 1214,362 1110,362" fill="url(#goldBox)"/>
    <text class="t-day" x="1168" y="340" text-anchor="middle" font-size="112">15</text>
    <text class="t-month" x="1153" y="395" text-anchor="middle" font-size="36" letter-spacing="1">MARCH</text>

    <path d="M455,434 H1212 A36.5,36.5 0 0 1 1212,507 H445 Z" fill="url(#goldFill)"/>
    <text class="t-register" x="478" y="484" font-size="38">REGISTER TODAY</text>
    <rect x="705" y="449" width="526" height="44" rx="22" fill="var(--navy)"/>
    <text class="t-url" x="968" y="478" text-anchor="middle" font-size="19">https://www.quillmarket.com.au/webinars</text>
  </svg>
  <p class="board-label board-label--facebook">FACEBOOK BANNER</p>

  <!-- LinkedIn banner -->
  <svg class="banner banner--linkedin" viewBox="0 0 1687 550">
    <rect width="1687" height="550" fill="var(--white)"/>
    <polygon points="0,0 853,0 756,550 0,550" fill="var(--navy)"/>
    <polygon role="img" aria-label="Photo of a speaker at a lectern addressing a seated audience in a dark auditorium" points="0,0 716,0 616,550 0,550" fill="url(#photoTone)"/>
    <polygon points="712,0 720,0 620,550 612,550" fill="url(#goldBox)"/>
    <text class="t-brand" x="383" y="135" text-anchor="middle" font-size="80">QUILL</text>
    <text class="t-brand" x="383" y="212" text-anchor="middle" font-size="80">MARKET</text>

    <polygon points="768,46 1156,46 1146,114 758,114" fill="url(#goldFill)"/>
    <text class="t-webinar" x="955" y="96" text-anchor="middle" font-size="44" letter-spacing="14">WEBINAR</text>
    <polygon points="1178,46 1640,46 1630,114 1168,114" fill="var(--navy)"/>
    <text class="t-time" x="1403" y="96" text-anchor="middle" font-size="40">7:00 PM – 8:00 PM <tspan class="t-time-zone">AEDT</tspan></text>

    <text class="t-kicker" x="873" y="189" font-size="58" fill="url(#goldText)">WAYS TO DEBUT A NOVEL</text>
    <rect x="873" y="199" width="690" height="3" fill="var(--navy)"/>
    <text class="t-headline" x="858" y="294" font-size="98">WITH SPARKLE</text>
    <text class="t-headline" x="846" y="389" font-size="98">&amp; FLAIR</text>

    <polygon points="1433,201 1563,201 1536,401 1406,401" fill="var(--navy)"/>
    <polygon points="1442,206 1556,206 1537,352 1423,352" fill="url(#goldBox)"/>
    <text class="t-day" x="1489" y="330" text-anchor="middle" font-size="118">15</text>
    <text class="t-month" x="1473" y="391" text-anchor="middle" font-size="38" letter-spacing="1">MARCH</text>

    <path d="M703,429 H1618 A38.5,38.5 0 0 1 1618,506 H693 Z" fill="url(#goldFill)"/>
    <text class="t-register" x="730" y="482" font-size="40">REGISTER TODAY</text>
    <rect x="993" y="447" width="640" height="42" rx="21" fill="var(--navy)"/>
    <text class="t-url" x="1313" y="475" text-anchor="middle" font-size="21" letter-spacing="1">https://www.quillmarket.com.au/webinars</text>
  </svg>
  <p class="board-label board-label--linkedin">LINKEDIN BANNER</p>

</div>
</body>
</html>
```